Personal Training

Personal Fitness Trainer
Sports Nutritionist
Individual and Group rates available
Certifications
Global Wellness Coaching Federation
Continental Athletic Studies Council

Industry/Entity Type

Fitness

Contact Information for Business Card

Dorinda Pellham
555-284-7163
vetrubel4@quintmail.example

```html
<!DOCTYPE html>
<html lang="en">
<head>
<meta charset="utf-8">
<title>Dorinda Pellham – Personal Training Business Card</title>
<link rel="stylesheet" href="https://fonts.googleapis.com/css2?family=Open+Sans:wght@400;600;700&display=swap">
<style>
  :root {
    --page-bg: #e9e6e1;
    --card-black: #0d0d0e;
    --card-charcoal: #1e1e20;
    --card-white: #f4f4f4;
    --accent-red: #ee2e44;
    --text-light: #f2f2f2;
    --text-soft: #d9d9d9;
    --text-dark: #2a2a2a;
    --photo-skin: #b8827a;
    --photo-pink: #c9707f;
    --photo-warm: #6a4a46;
    --badge-gold: #c9a64a;
  }
  * { margin: 0; padding: 0; box-sizing: border-box; }
  html, body {
    width: 1200px; height: 1023px; overflow: hidden;
    background: var(--page-bg);
    font-family: "Open Sans", Arial, sans-serif;
  }
  .canvas {
    position: relative; width: 1200px; height: 1023px;
  }
  .card {
    position: absolute; left: 232px;
    width: 735px; height: 420px;
    overflow: hidden;
    border-radius: 4px;
    box-shadow: 0 10px 28px rgba(0,0,0,.25);
  }
  .card--front { top: 64px; }
  .card--back { top: 540px; }

  /* Front */
  .front-shapes { position: absolute; inset: 0; }
  .front-photo {
    position: absolute; left: 0; top: 210px; width: 380px; height: 210px;
    background:
      radial-gradient(ellipse 45% 50% at 40% 55%, var(--photo-pink) 0%, var(--photo-skin) 35%, var(--photo-warm) 65%, transparent 100%);
    opacity: .9;
  }
  .front-contact {
    position: absolute; left: 110px; top: 70px; width: 300px;
    text-align: center;
  }
  .contact-name {
    color: var(--accent-red);
    font-weight: 700; font-size: 28px; line-height: 38px; letter-spacing: .3px;
    white-space: nowrap;
  }
  .contact-line {
    color: var(--text-light);
    font-size: 17px; line-height: 28px;
    white-space: nowrap;
  }
  .contact-name + .contact-line { margin-top: 14px; }
  .cert-mark {
    position: absolute; left: 520px; top: 120px; width: 200px;
    display: flex; flex-direction: column; align-items: center; gap: 14px;
    text-align: center;
  }
  .cert-dot {
    width: 96px; height: 96px; border-radius: 50%;
    background: var(--badge-gold);
  }
  .cert-name {
    color: var(--text-dark); font-size: 15px; font-weight: 600; line-height: 21px;
  }

  /* Back */
  .back-photo {
    position: absolute; inset: 0;
    background:
      radial-gradient(ellipse 30% 40% at 30% 45%, rgba(120,60,70,.55), transparent 75%),
      radial-gradient(ellipse 25% 35% at 65% 55%, rgba(150,80,80,.4), transparent 75%),
      linear-gradient(160deg, var(--card-charcoal), var(--card-black));
  }
  .back-services {
    position: absolute; inset: 0;
    display: flex; flex-direction: column; justify-content: center; align-items: center;
    background: rgba(0,0,0,.35);
  }
  .service-line {
    color: var(--text-soft);
    font-size: 24px; line-height: 34px; letter-spacing: .5px;
  }
</style>
</head>
<body>
<main class="canvas">

  <section class="card card--front" aria-label="Business card front">
    <svg class="front-shapes" width="735" height="420" viewBox="0 0 735 420" aria-hidden="true">
      <rect width="735" height="420" fill="var(--card-black)"/>
      <path d="M440,0 Q455,230 560,420 L735,420 L735,0 Z" fill="var(--card-white)"/>
      <path d="M430,0 Q445,230 548,420" fill="none" stroke="var(--accent-red)" stroke-width="12"/>
    </svg>
    <div class="front-photo" role="img" aria-label="Photo of the trainer posing in fitness wear"></div>
    <div class="front-contact">
      <p class="contact-name">Dorinda Pellham</p>
      <p class="contact-line">555-284-7163</p>
      <p class="contact-line">vetrubel4@quintmail.example</p>
    </div>
    <div class="cert-mark">
      <span class="cert-dot" aria-hidden="true"></span>
      <p class="cert-name">Global Wellness Coaching Federation</p>
    </div>
  </section>

  <section class="card card--back" aria-label="Business card back">
    <div class="back-photo" role="img" aria-label="Faded photo of a training session in the gym"></div>
    <div class="back-services">
      <p class="service-line">Personal Fitness Trainer</p>
      <p class="service-line">Sports Nutritionist</p>
      <p class="service-line">Individual &amp; Group rates available</p>
    </div>
  </section>

</main>
</body>
</html>
```